Letterhead Design for Law Firm that Specializes in Property Damage Litigation

We are looking for a redesign of our letterhead. Our current letterhead lists all of our current staff members and we'd like to come up with a design that does NOT list all of the staff members so that it does not need to be updated with every newly hired employee. Must be in editable format.

We are a law firm that specializes in property damage, so we need something that is professional, yet modern. The final design should use our existing logo and should use a blue color scheme (alternate colors would be gray, black, and white).

Industry/Entity Type

Legal

Colors
0054AA
0677BA
7BADD7
CADEEF
E8F1F8

```html
<!DOCTYPE html>
<html lang="en">
<head>
<meta charset="utf-8">
<title>Harlow Pryce &amp; Ventura – Letterhead</title>
<link rel="stylesheet" href="https://fonts.googleapis.com/css2?family=Cinzel:wght@600&family=Barlow:wght@500&family=Montserrat:wght@400&display=swap">
<style>
  :root {
    --paper: #eceef1;
    --navy: #1f3a70;
    --gray: #6b6e72;
    --ink: #2b2f36;
    --icon: #5f6f8a;
    --mark-soft: #d7e3ec;
  }
  * { margin: 0; padding: 0; box-sizing: border-box; }
  html, body { width: 849px; height: 1200px; overflow: hidden; background: var(--paper); }
  .letterhead { position: relative; width: 849px; height: 1200px; overflow: hidden; background: var(--paper); }

  .brand-square {
    position: absolute; left: 92px; top: 78px;
    width: 84px; height: 84px;
    background: var(--navy);
  }
  .firm-name {
    position: absolute; left: 202px; top: 74px;
    font-family: "Cinzel", "Times New Roman", serif;
    font-weight: 600; font-size: 27px; line-height: 29px;
    letter-spacing: 1.5px; color: var(--navy);
  }
  .tagline {
    position: absolute; left: 86px; top: 176px;
    font-family: "Barlow", Arial, sans-serif;
    font-weight: 500; font-size: 10.5px; letter-spacing: 3.6px;
    color: var(--gray);
  }

  .name-watermark {
    position: absolute; right: 40px; top: 720px;
    text-align: right;
    font-family: "Cinzel", "Times New Roman", serif;
    font-weight: 600; font-size: 76px; line-height: 92px;
    letter-spacing: 2px; color: var(--mark-soft);
    white-space: nowrap;
  }

  .contact-list {
    position: absolute; left: 81px; top: 1067px;
    list-style: none;
    font-family: "Montserrat", Arial, sans-serif;
    font-size: 10.5px; line-height: 13px; color: var(--ink);
  }
  .contact-item { display: flex; align-items: flex-start; gap: 14px; margin-bottom: 9px; }
  .contact-item svg { width: 14px; height: 14px; flex: none; stroke: var(--icon); fill: none; stroke-width: 1.1; }
  .contact-item.address { margin-top: -3px; }
</style>
</head>
<body>
  <main class="letterhead">
    <div class="brand-square"></div>
    <div class="firm-name">HARLOW<br>PRYCE &amp;<br>VENTURA</div>
    <div class="tagline">THE PROPERTY DAMAGE ATTORNEYS</div>

    <div class="name-watermark" aria-hidden="true">HARLOW<br>PRYCE &amp;<br>VENTURA</div>

    <ul class="contact-list">
      <li class="contact-item">
        <svg viewBox="0 0 14 14"><path d="M3 1.5l2 2.6-1.2 1.4c.8 1.8 2.3 3.3 4.1 4.1l1.4-1.2 2.6 2-1.3 2c-5 0-9.4-4.4-9.4-9.4z"/></svg>
        <span>(555) 014-2290</span>
      </li>
      <li class="contact-item">
        <svg viewBox="0 0 14 14"><rect x="1" y="3" width="12" height="8.5" rx="1"/><path d="M1.3 3.4L7 8l5.7-4.6"/></svg>
        <span>hello@harlowpryce.com</span>
      </li>
      <li class="contact-item">
        <svg viewBox="0 0 14 14"><circle cx="7" cy="7" r="5.6"/><ellipse cx="7" cy="7" rx="2.4" ry="5.6"/><path d="M1.4 7h11.2M2.3 4.2h9.4M2.3 9.8h9.4"/></svg>
        <span>www.hpvlegal.com</span>
      </li>
      <li class="contact-item address">
        <svg viewBox="0 0 14 14"><path d="M7 13s-4.2-4.4-4.2-7.4a4.2 4.2 0 018.4 0C11.2 8.6 7 13 7 13z"/><circle cx="7" cy="5.6" r="1.5"/></svg>
        <span>880 Linden Avenue Suite 410,<br>Marlow City, PA 19000</span>
      </li>
    </ul>
  </main>
</body>
</html>
```